Hinge Helper Plus VEHICLE WRAP for Pick Up Trucks with Canopies.

I'm looking for a Bright Eye Catching vehicle wrap for our pick up trucks. Not Vans!
We are a Residential and Commercial garage door repair company located in Coquitlam BC.
A photo of one of our service vehicles with our old name is attached.
Our logo is attached.
I would like Green and shades of Yellow/Gold incorporated.
https://photos.quillmarket-example.com/images/amber-swirl-backdrop/310274855
*The phrase, "Trust Our Craftsmen To Keep You Safe and Secure".
*HHPlus.ca
*604.555.2917
*I will add a QR code image to the files asap
I don't want it crowded but our services include Garage Doors, Parking Gates, Warehouse Doors, and More.
Feel free to search other door company vehicle signage for what they have and what they don't have in their designs.

Target Market(s)

Apartment Security Gate Service and Garage Door Repair.

Industry/Entity Type

Residential, Commercial, Industrial Door Repair

Colors

Designer to choose colors to be used in the design.

Requirements
Must have
• Use the Quillmarket Yellow Abstract attached. Don't want it crowded but our services include Garage Doors, Parking Gates, Warehouse Doors.

```html
<!DOCTYPE html>
<html lang="en">
<head>
<meta charset="utf-8">
<title>Hinge Helper Plus – Vehicle Wrap Panels</title>
<link rel="stylesheet" href="https://fonts.googleapis.com/css2?family=Barlow+Condensed:wght@500;600&family=Barlow:wght@500&family=Open+Sans:wght@400&display=swap">
<style>
  :root {
    --backdrop: #333333;
    --panel: #ffffff;
    --ink: #111111;
    --navy: #13262f;
    --gold: #fcc94d;
    --gold-deep: #e8b414;
    --qr-grey: #9b9b9b;
  }
  * { box-sizing: border-box; margin: 0; padding: 0; }
  html, body { width: 1200px; height: 1045px; overflow: hidden; }
  body { background: var(--backdrop); position: relative; font-family: "Barlow Condensed", sans-serif; color: var(--ink); }

  .panel { position: absolute; background: var(--panel); overflow: hidden; }
  .panel-side { left: 280px; top: 123px; width: 637px; height: 242px; }
  .panel-rear { left: 329px; top: 408px; width: 539px; height: 514px; }

  .backdrop-art {
    position: absolute; left: 0; right: 0; bottom: 0;
    background: linear-gradient(90deg, var(--gold) 0%, var(--gold-deep) 25%, #7a6a30 50%, #3b3f31 68%, var(--navy) 85%);
  }
  .panel-side .backdrop-art { height: 62px; }
  .panel-rear .backdrop-art { height: 124px; }

  .tagline { position: absolute; left: 35px; top: 22px; font-weight: 600; font-size: 27px; line-height: 32px; }
  .tagline-rule { position: absolute; left: 0; top: 123px; width: 250px; height: 3px; background: linear-gradient(90deg, var(--gold-deep) 0%, var(--gold) 60%, rgba(252,201,77,0) 100%); }

  .phone { position: absolute; display: flex; align-items: center; gap: 3px; font-weight: 500; }
  .phone-icon { flex: none; }

  .brand { position: absolute; display: flex; align-items: center; gap: 8px; font-weight: 600; color: var(--navy); white-space: nowrap; }
  .brand-mark { flex: none; background: var(--gold); }

  .services { position: absolute; list-style: none; font-weight: 600; }
  .services li { display: flex; align-items: center; }
  .services svg { flex: none; }

  .qr-slot { position: absolute; background: var(--qr-grey); }
  .web { position: absolute; font-family: "Open Sans", sans-serif; font-weight: 400; white-space: nowrap; }

  .panel-side .phone { left: 26px; top: 133px; font-size: 23px; }
  .panel-side .brand { left: 250px; top: 74px; width: 191px; justify-content: center; font-size: 27px; }
  .panel-side .brand-mark { width: 14px; height: 14px; }
  .panel-side .services { left: 462px; top: 24px; font-size: 19px; line-height: 23.5px; }
  .panel-side .services li { gap: 6px; }
  .panel-side .qr-slot { left: 516px; top: 96px; width: 47px; height: 47px; }
  .panel-side .web { left: 538px; top: 148px; transform: translateX(-50%); font-size: 14px; }

  .panel-rear .brand { left: 110px; top: 88px; width: 320px; justify-content: center; font-size: 36px; }
  .panel-rear .brand-mark { width: 20px; height: 20px; }
  .panel-rear .services { left: 54px; top: 199px; font-size: 26px; line-height: 32px; }
  .panel-rear .services li { gap: 7px; }
  .panel-rear .phone { left: 55px; top: 302px; font-size: 24px; }
  .panel-rear .web { left: 82px; top: 333px; font-size: 20px; }
  .panel-rear .qr-slot { left: 377px; top: 210px; width: 100px; height: 100px; }
  .caption { position: absolute; left: 326px; top: 317px; width: 200px; text-align: center; font-family: "Barlow", sans-serif; font-weight: 500; font-size: 13.5px; line-height: 17.2px; }
</style>
</head>
<body>

<svg width="0" height="0" style="position:absolute" aria-hidden="true">
  <defs>
    <linearGradient id="arrow-fill" x1="0" y1="0" x2="1" y2="0">
      <stop offset="0" stop-color="#f4f27a"/><stop offset="1" stop-color="#e8b414"/>
    </linearGradient>
    <symbol id="bullet" viewBox="0 0 20 14"><path d="M0 0 L20 7 L0 14 L5 7 Z" fill="url(#arrow-fill)"/></symbol>
    <symbol id="handset" viewBox="0 0 24 24">
      <circle cx="12" cy="12" r="12" fill="#13262f"/>
      <path d="M8.2 5.5c.5-.3 1.1-.1 1.4.4l1.3 2.3c.3.5.2 1.1-.2 1.4l-1 .8c.6 1.6 1.8 3 3.2 3.9l.9-.9c.4-.4 1-.4 1.4-.1l2.2 1.5c.5.3.6 1 .3 1.5l-.9 1.3c-.5.7-1.4 1-2.2.7-3.8-1.4-6.6-4.6-7.5-8.6-.2-.8.1-1.6.8-2.1z" fill="#fff"/>
    </symbol>
  </defs>
</svg>

<section class="panel panel-side" aria-label="Truck side panel">
  <div class="backdrop-art" role="img" aria-label="Gold and navy abstract background artwork"></div>

  <p class="tagline">Trust Our Craftsmen<br>To Keep You Safe<br>and Secure</p>
  <div class="tagline-rule"></div>
  <p class="phone"><svg class="phone-icon" width="21" height="21"><use href="#handset"/></svg>604.555.2917</p>

  <div class="brand"><span class="brand-mark"></span>Hinge Helper Plus</div>

  <ul class="services">
    <li><svg width="13" height="9"><use href="#bullet"/></svg>Garage Doors</li>
    <li><svg width="13" height="9"><use href="#bullet"/></svg>Parking Gates</li>
    <li><svg width="13" height="9"><use href="#bullet"/></svg>Warehouse Doors</li>
  </ul>
  <div class="qr-slot" role="img" aria-label="QR code placeholder"></div>
  <p class="web">HHPlus.ca</p>
</section>

<section class="panel panel-rear" aria-label="Truck rear panel">
  <div class="backdrop-art" role="img" aria-label="Gold and navy abstract background artwork"></div>

  <div class="brand"><span class="brand-mark"></span>Hinge Helper Plus</div>

  <ul class="services">
    <li><svg width="17" height="12"><use href="#bullet"/></svg>Garage Doors</li>
    <li><svg width="17" height="12"><use href="#bullet"/></svg>Parking Gates</li>
    <li><svg width="17" height="12"><use href="#bullet"/></svg>Warehouse Doors</li>
  </ul>
  <p class="phone"><svg class="phone-icon" width="22" height="22"><use href="#handset"/></svg>604.555.2917</p>
  <p class="web">HHPlus.ca</p>

  <div class="qr-slot" role="img" aria-label="QR code placeholder"></div>
  <p class="caption">Residential, Commercial<br>&amp; Industrial Apartment<br>Gate Specialists</p>
</section>

</body>
</html>
```